CEO of company needs clear business card that stands out from the rest

I need a clear business card (standard credit card size) for the CEO/Founder of our company...Brightfield Counseling. We would like to see designs that use our logo colors, which are khaki, chocolate brown, and gray. The card should be an edgy design, maybe where half the card is transparent with curves on the card, or a textured card where the logo is transparent, I don't care much for white cards. The final design should communicate a funky, edgy, and modern look, as well as stand out to have the "WOW" factor. The information we need on the card would be Name, Title, Toll free number, Phone Number, address, email address, and website.

*PLEASE SEND FRONT AND BACK OF CARDS

Card is two sided front and back please give us your front and back designs

The card should be an edgy design, maybe where half the card is transparent with curves on the card, or a textured card where the logo is transparent, I don't care much for white cards. The final design should communicate a funky, edgy, and modern look, as well as stand out to have the "WOW" factor.

Please follow these guidelines for the card

SPECS (card):

2.125 (h) x 3.375 (w) card size after cut

2.375 (h) x 3.625 (w) card with bleed

300 dpi

cmyk

1/8 bleed

allow 1/8 border for live area

I will also attached the pdf for the information listed above which includes a diagram of the card

 

All the cards need to have rounded edges

I just updated a card as an example of how you can use different fonts on a single business card, look how the name is written in script, so what I am saying is make this a card you will be proud to design and put it in your portfolio 

Reason: this race is really close and I am working with 2 designers to fine tune their designs and the weekend is slowing us down

• Our Logo
MUST HAVE PARTS OF CARD THAT ARE TRANSPARENT. See ideas that are attached.
Card is two sided front and back
• The final design should communicate a funky, edgy, and modern look, as well as stand out to have the "WOW" factor. The information we need on the card would be Name, Title, Toll free number, Phone Number, address, email address, and website.

```html
<!DOCTYPE html>
<html lang="en">
<head>
<meta charset="utf-8">
<title>Brightfield Counseling – Business Card</title>
<link rel="stylesheet" href="https://fonts.googleapis.com/css2?family=Montserrat:wght@700&family=Questrial&display=swap">
<style>
  :root {
    --stage: #1f1b18;
    --chocolate: #7a3d0c;
    --chocolate-deep: #5e2e08;
    --card-white: #ffffff;
    --gray: #8a8a8a;
    --gray-dark: #5c5c5c;
    --text-light: #f4e9dd;
  }
  * { margin: 0; padding: 0; box-sizing: border-box; }
  html, body { width: 1200px; height: 675px; overflow: hidden; }
  body {
    background: var(--stage);
    font-family: "Questrial", "Century Gothic", sans-serif;
    position: relative;
  }
  .card {
    position: absolute;
    top: 167px;
    width: 540px;
    height: 340px;
    border-radius: 22px;
    overflow: hidden;
  }
  .card--front { left: 40px; background: var(--card-white); }
  .card--back { left: 620px; background: linear-gradient(135deg, var(--chocolate) 0%, var(--chocolate-deep) 100%); }

  .brand {
    position: absolute;
    display: flex;
    align-items: center;
    gap: 10px;
    font-family: "Questrial", "Century Gothic", sans-serif;
    font-size: 25px;
    white-space: nowrap;
  }
  .brand__dot { width: 22px; height: 22px; border-radius: 50%; flex: none; }
  .card--front .brand { left: 30px; top: 192px; color: var(--chocolate); }
  .card--front .brand__dot { background: var(--gray); }
  .card--back .brand { left: 90px; top: 120px; color: var(--card-white); font-size: 28px; }
  .card--back .brand__dot { background: var(--card-white); }

  .identity { position: absolute; left: 318px; top: 78px; }
  .identity__name {
    font-family: "Montserrat", sans-serif;
    font-weight: 700;
    font-size: 16px;
    color: var(--chocolate);
  }
  .identity__title { font-size: 13px; color: var(--gray-dark); margin-top: 1px; }

  .contact-band {
    position: absolute;
    left: 310px; right: 0;
    top: 118px; height: 122px;
    background: var(--chocolate);
    padding: 16px 0 0 16px;
    color: var(--text-light);
    font-size: 11.5px;
    line-height: 17px;
  }
  .contact-band__row { display: flex; align-items: center; gap: 6px; white-space: nowrap; }
  .contact-band__row svg { width: 11px; height: 11px; flex: none; fill: var(--text-light); }

  .website {
    position: absolute;
    font-family: "Montserrat", sans-serif;
    font-weight: 700;
    font-size: 11.5px;
    white-space: nowrap;
  }
  .card--front .website { left: 330px; top: 256px; color: var(--chocolate); }
  .card--back .website { left: 180px; top: 240px; color: var(--card-white); }

  .edge-tab {
    position: absolute;
    left: 0; top: 130px;
    width: 22px; height: 110px;
    background: var(--card-white);
  }
</style>
</head>
<body>
  <section class="card card--front" aria-label="Card front">
    <div class="brand"><span class="brand__dot"></span>Brightfield Counseling</div>

    <div class="identity">
      <p class="identity__name">Miriam Caldwell</p>
      <p class="identity__title">Co-Founder</p>
    </div>

    <div class="contact-band">
      <p class="contact-band__row">27 Rue Verlaine</p>
      <p class="contact-band__row">1060 Saint-Gilles, Belgium</p>
      <p class="contact-band__row">
        <svg viewBox="0 0 12 12" aria-hidden="true"><rect x="0" y="0" width="12" height="12" rx="2"/><path d="M3.5 2.5c.5 0 1 1.4 1 1.8 0 .4-.6.6-.5 1 .3.9 1 1.6 1.9 1.9.4.1.6-.5 1-.5s1.8.5 1.8 1c0 .8-.8 1.6-1.6 1.6C4.6 9.3 2.7 7.4 2.7 4.9c0-.9.1-2.4.8-2.4z" fill="#7a3d0c"/></svg>
        +1.555.014.2387
      </p>
      <p class="contact-band__row">
        <svg viewBox="0 0 12 12" aria-hidden="true"><rect x="0" y="0" width="12" height="12" rx="2"/><path d="M3.5 2.5c.5 0 1 1.4 1 1.8 0 .4-.6.6-.5 1 .3.9 1 1.6 1.9 1.9.4.1.6-.5 1-.5s1.8.5 1.8 1c0 .8-.8 1.6-1.6 1.6C4.6 9.3 2.7 7.4 2.7 4.9c0-.9.1-2.4.8-2.4z" fill="#7a3d0c"/></svg>
        +32.470.118.204 - Direct
      </p>
      <p class="contact-band__row">
        <svg viewBox="0 0 12 12" aria-hidden="true"><rect x="0" y="2" width="12" height="8" rx="1"/><path d="M1 3l5 4 5-4" stroke="#7a3d0c" stroke-width="1.2" fill="none"/></svg>
        miriam@brightfieldcounseling.com
      </p>
    </div>

    <p class="website">www.brightfieldcounseling.com</p>
  </section>

  <section class="card card--back" aria-label="Card back">
    <div class="edge-tab"></div>
    <div class="brand"><span class="brand__dot"></span>Brightfield Counseling</div>
    <p class="website">www.brightfieldcounseling.com</p>
  </section>
</body>
</html>
```